Consultant company (start up) needs a bold, yet simple web design

We need a we design for "Kestrel Analys & Rådgivning". As our name implies we are a consultant firm helping companies with public sector business (tenders), but also helping the buyer side. We provide market research and reports, advice (legal and business) and hands-on-help with tender applications (projectleader; analysing critiera and texts, document reviews, etc). We have a rather uniqe position in our market with our mixed competences of branding and market communication, formal management systems, and public tenders.

We have a strong drive to make tender business simple for our clients: we will take care of the complicated!

We want our web design to be bold, yet clean and simple, communicating:

Competence; Commitment, Simplicity (for the customer).
Updates

Reason: For different reasons our web project was put on hold/was delayed a few days. As of today we are kicking life into it again, and expect to come back with feedback on designs in the next days. Best regards, Henrik

Target Market(s)

We primarily help companies aiming for public contracts.

Industry/Entity Type

Business Consultant

Contact Information for Business Card

Company logo; First name, Last name, Titel, webadress; personal e-mail
Maybe: a motto like "Offentliga affärer. Enklare" ("Public business. Made simple.")

Coding

Coded - Design and coding required

Font styles to use
Sans Serif

Colors

Designer to choose colors to be used in the design.

Requirements
Must have
• Dual language (Swedish and English)
• Responsive design, many people will view our webpage on their phone or ipad.
• We want to make our position clear, stating what distinguishes us from "the rest of the pack" in maybe with on the starting page.
• [Will update brief; need to think this through]
Nice to have
• We have our logo in three colours. Green is our first. We are not yet sure why we have the different colurs. Maybe (just maybe!) the different colours can be put to use?
• We need help with the choice of images.
Should not have
• Never boring.

```html
<!DOCTYPE html>
<html lang="en">
<head>
<meta charset="utf-8">
<title>Kestrel Analys &amp; Rådgivning</title>
<link rel="stylesheet" href="https://fonts.googleapis.com/css2?family=Lato:wght@400;700&family=Open+Sans:ital,wght@0,400;0,600;1,400&display=swap">
<style>
:root{
  --green:#3e8a28;
  --green-bright:#58a82c;
  --ink:#222;
  --text:#555;
  --muted:#777;
  --line:#ddd;
  --soft:#f2f2f2;
  --white:#fff;
}
*{box-sizing:border-box;margin:0;padding:0}
html,body{width:1200px;height:2715px;overflow:hidden;background:var(--white)}
body{position:relative;font-family:"Open Sans",Arial,sans-serif;color:var(--text)}
.abs{position:absolute}
.heading{font-family:"Lato",Arial,sans-serif;color:var(--ink);font-weight:700}

/* header */
.site-header{position:absolute;left:0;top:0;width:1200px;height:95px;background:var(--white);box-shadow:0 1px 4px rgba(0,0,0,.08);z-index:2}
.brand{position:absolute;left:98px;top:24px;display:flex;align-items:center;gap:12px;font-family:"Lato",sans-serif;font-weight:700;font-size:22px;color:var(--green)}
.brand-dot{width:34px;height:34px;border-radius:50%;background:var(--green)}
.topbar{position:absolute;top:16px;right:98px;display:flex;align-items:center;gap:26px;font-size:15px;color:var(--ink)}
.topbar span{display:flex;align-items:center;gap:8px}
.icon-badge{width:28px;height:28px;border-radius:50%;border:1px solid var(--line);display:inline-flex;align-items:center;justify-content:center}
.main-nav{position:absolute;top:58px;right:92px;display:flex;gap:28px;font-family:"Lato",sans-serif;font-size:17px;color:var(--ink);align-items:center}
.main-nav .active{color:var(--green-bright)}

/* hero */
.hero{position:absolute;left:0;top:95px;width:1200px;height:460px;background:linear-gradient(120deg,#3a3a3a,#6d6d6d 40%,#9a9a9a 65%,#4e4e4e)}
.hero-shade{position:absolute;inset:0;background:rgba(0,0,0,.35)}
.hero-title{position:absolute;top:118px;width:100%;text-align:center;font-family:"Lato",sans-serif;font-weight:700;font-size:56px;color:var(--white)}
.hero-sub{position:absolute;top:192px;width:100%;text-align:center;font-size:23px;line-height:35px;color:var(--white)}
.hero-btn{position:absolute;left:495px;top:285px;width:210px;height:48px;border:2px solid var(--white);border-radius:24px;color:var(--white);font-family:"Lato",sans-serif;font-weight:700;font-size:16px;display:flex;align-items:center;justify-content:center}
.hero-dots{position:absolute;top:401px;left:560px;display:flex;gap:8px}
.hero-dots i{width:12px;height:12px;border-radius:50%;border:2px solid var(--white)}
.hero-dots i:first-child{background:var(--white)}

/* welcome */
.welcome-title{left:100px;top:632px;font-size:28px;line-height:38px}
.welcome-text{left:100px;top:728px;width:460px;font-size:12.5px;line-height:23px}
.welcome-text p+p{margin-top:23px}
.outline-btn{border:1.5px solid var(--text);border-radius:17px;color:var(--green-bright);font-family:"Lato",sans-serif;font-weight:700;font-size:13px;display:flex;align-items:center;justify-content:center}
.welcome-btn{left:100px;top:897px;width:115px;height:33px}
.video-frame{left:615px;top:618px;width:487px;height:302px;border:1px solid #ccc;padding:5px;background:var(--white);box-shadow:0 0 3px rgba(0,0,0,.15)}
.video-frame .media{width:100%;height:100%;background:linear-gradient(135deg,#c9c9c9,#f1f1f1 45%,#8fb5d8 70%,#e8e8e8)}
.play{position:absolute;left:216px;top:124px;width:56px;height:56px;border-radius:50%;background:#1b1b1b}

/* services */
.services{position:absolute;left:0;top:1005px;width:1200px;height:467px;background:var(--soft)}
.section-title{position:absolute;width:100%;text-align:center;font-size:26px}
.service{position:absolute;top:127px;width:240px;text-align:center}
.service-ring{width:138px;height:138px;margin:0 auto;border:2.5px solid var(--green);border-radius:50%;display:flex;align-items:center;justify-content:center}
.service h3{margin-top:27px;font-family:"Lato",sans-serif;font-weight:700;font-size:17.5px;color:var(--ink)}
.service p{margin-top:14px;font-size:12px;line-height:22px}
.read-more{display:block;margin-top:14px;font-family:"Lato",sans-serif;font-weight:700;font-size:13px;color:var(--green-bright)}
.arrow{position:absolute;width:38px;height:38px;border-radius:50%;border:1.5px solid #999;display:flex;align-items:center;justify-content:center}

/* blog */
.blog-card{position:absolute;top:1612px;width:324px}
.blog-photo{position:relative;height:212px;border:1px solid #ccc;padding:4px;background:var(--white)}
.blog-photo .media{width:100%;height:100%}
.date{position:absolute;left:-6px;top:138px;width:46px;height:62px;background:var(--green-bright);color:var(--white);text-align:center;font-family:"Lato",sans-serif}
.date b{display:block;font-size:24px;line-height:30px;margin-top:4px}
.date span{font-size:14px}
.blog-card h3{margin-top:18px;font-family:"Lato",sans-serif;font-weight:700;font-size:19.5px;color:var(--ink)}
.blog-card p{margin-top:10px;font-size:12px;line-height:23px}
.blog-meta{margin-top:12px;padding-top:14px;border-top:1px solid var(--line);font-size:12px;display:flex;gap:20px}
.blog-meta span{display:flex;align-items:center;gap:6px}

/* testimonials */
.testimonials{position:absolute;left:0;top:2040px;width:1200px;height:330px;background:var(--green)}
.testimonials .section-title{color:var(--white);top:52px}
.quote{position:absolute;top:125px;width:340px}
.avatar{position:absolute;left:0;top:0;width:76px;height:76px;border-radius:50%;border:3px solid var(--white);background:linear-gradient(#cfcfcf,#9e9e9e)}
.quote-body{position:absolute;left:92px;top:6px;width:240px;color:var(--white)}
.quote-body p{font-style:italic;font-size:12px;line-height:24px}
.quote-body p::before{content:"\201C";font-family:Georgia,serif;font-size:26px;font-style:normal;line-height:0;margin-right:8px;vertical-align:-8px}
.quote-body h4{margin-top:14px;font-size:10px;font-weight:600;text-transform:uppercase}
.quote-body small{display:block;font-style:italic;font-size:9.5px;margin-top:3px}
.testimonials .arrow{border-color:var(--white)}

/* footer */
.footer-brand{left:100px;top:2500px;display:flex;align-items:center;gap:12px;font-family:"Lato",sans-serif;font-weight:700;font-size:21px;color:var(--green)}
.footer-col h4{font-family:"Lato",sans-serif;font-weight:700;font-size:18px;color:var(--ink);margin-bottom:18px}
.footer-col{font-size:12.5px;line-height:20.5px;color:var(--text)}
.email-field{margin-top:12px;width:255px;border-bottom:1px solid #bbb;padding:6px 10px;color:#999;font-size:12px}
.subscribe{margin-top:14px;width:100px;height:30px}
.contact-row{display:flex;gap:16px;margin-bottom:20px}
.footer-rule{left:100px;top:2635px;width:1000px;height:1px;background:var(--line)}
.copyright{left:100px;top:2668px;font-size:12px}
.social{left:975px;top:2662px;display:flex;gap:9px}
.social i{width:24px;height:24px;border-radius:50%;border:1px solid var(--green)}
</style>
</head>
<body>

<header class="site-header">
  <div class="brand"><span class="brand-dot"></span>Kestrel Analys &amp; Rådgivning</div>
  <div class="topbar">
    <span>
      <svg width="20" height="13" viewBox="0 0 20 13"><rect width="20" height="13" fill="#d22"/><rect y="5" width="20" height="3" fill="#fff"/><rect x="8" width="4" height="13" fill="#fff"/></svg>
      Eng
      <svg width="10" height="6" viewBox="0 0 10 6"><path d="M1 1l4 4 4-4" stroke="#333" fill="none" stroke-width="1.5"/></svg>
    </span>
    <span><span class="icon-badge"><svg width="14" height="14" viewBox="0 0 24 24"><path fill="#3e8a28" d="M6.6 10.8a15 15 0 006.6 6.6l2.2-2.2c.3-.3.7-.4 1-.2 1.1.4 2.3.6 3.6.6.6 0 1 .4 1 1V20c0 .6-.4 1-1 1A17 17 0 013 4c0-.6.4-1 1-1h3.5c.6 0 1 .4 1 1 0 1.3.2 2.5.6 3.6.1.3 0 .7-.2 1z"/></svg></span>1 555 010 0199</span>
    <span><span class="icon-badge" style="background:var(--green);border-color:var(--green)"><svg width="13" height="10" viewBox="0 0 13 10"><rect width="13" height="10" fill="#fff"/><path d="M0 0l6.5 5L13 0" stroke="#3e8a28" fill="none"/></svg></span>info@kestrelanalys.se</span>
  </div>
  <nav class="main-nav">
    <span class="active">Home</span><span>About Us</span><span>Services</span><span>Industries</span><span>Resources</span><span>Blog</span><span>Contact Us</span>
    <svg width="16" height="16" viewBox="0 0 16 16"><circle cx="6.5" cy="6.5" r="5" stroke="#222" stroke-width="2" fill="none"/><path d="M10 10l5 5" stroke="#222" stroke-width="2"/></svg>
  </nav>
</header>

<section class="hero">
  <div class="abs" style="inset:0" role="img" aria-label="Business people reviewing charts and documents at a desk"></div>
  <div class="hero-shade"></div>
  <h1 class="hero-title">Kestrel Analys &amp; Rådgivning</h1>
  <p class="hero-sub">We are a consultant firm helping companies with public sector<br>business (tenders), but also helping the buyer side.</p>
  <div class="hero-btn">GET MORE INFO &gt;&gt;</div>
  <div class="hero-dots"><i></i><i></i><i></i><i></i></div>
</section>

<section class="welcome">
  <h2 class="abs heading welcome-title">WELCOME TO KESTREL ANALYS<br>&amp; RÅDGIVNING</h2>
  <div class="abs welcome-text">
    <p>At vero eos et accusamus et iusto odio dignissimos ducimus qui blanditiis praesen tium voluptatum deleniti atque corrupti quo.</p>
    <p>Dolores et quas molestias excepturi sint occaecati cupiditate non provident, simil ique sunt in culpa qui officia deserunt mollitia animi, id est laborum et dolorum fu t harum quidem rerum facilis est et expedita di.</p>
  </div>
  <div class="abs outline-btn welcome-btn">READ MORE &gt;&gt;</div>
  <div class="abs video-frame">
    <div class="media" role="img" aria-label="Hand with pen over printed pie and bar charts"></div>
    <div class="play"><svg width="56" height="56" viewBox="0 0 56 56"><path d="M23 18l15 10-15 10z" fill="#fff"/></svg></div>
  </div>
</section>

<section class="services">
  <h2 class="section-title heading" style="top:76px">OUR SERVICES</h2>
  <div class="arrow" style="left:32px;top:222px"><svg width="10" height="14"><path d="M8 1L2 7l6 6" stroke="#888" fill="none" stroke-width="1.5"/></svg></div>
  <div class="arrow" style="left:1128px;top:222px"><svg width="10" height="14"><path d="M2 1l6 6-6 6" stroke="#888" fill="none" stroke-width="1.5"/></svg></div>

  <div class="service" style="left:88px">
    <div class="service-ring"><svg width="70" height="60" viewBox="0 0 70 60"><rect x="6" y="30" width="9" height="22" fill="#3e8a28"/><rect x="20" y="22" width="9" height="30" fill="#3e8a28"/><rect x="34" y="34" width="9" height="18" fill="#3e8a28"/><circle cx="54" cy="42" r="11" fill="none" stroke="#3e8a28" stroke-width="4"/><path d="M6 22l14-10 14 8 22-16" stroke="#3e8a28" stroke-width="3" fill="none"/><path d="M2 54h66" stroke="#3e8a28" stroke-width="3"/></svg></div>
    <h3>Market research &amp; reports</h3>
    <p>Nam libero tempore, cum soluta nobis<br>est eligendi optio cumque nihi</p>
    <span class="read-more">READ MORE &gt;&gt;</span>
  </div>
  <div class="service" style="left:349px">
    <div class="service-ring"><svg width="56" height="66" viewBox="0 0 56 66"><path d="M4 2h34l14 14v48H4z" fill="none" stroke="#3e8a28" stroke-width="3"/><path d="M12 22h20M12 30h32M12 38h32M12 46h32M12 54h24" stroke="#3e8a28" stroke-width="3"/><circle cx="20" cy="12" r="5" fill="#3e8a28"/></svg></div>
    <h3>Advice (legal and business)</h3>
    <p>Nam libero tempore, cum soluta nobis<br>est eligendi optio cumque nihi</p>
    <span class="read-more">READ MORE &gt;&gt;</span>
  </div>
  <div class="service" style="left:611px">
    <div class="service-ring"><svg width="66" height="70" viewBox="0 0 66 70"><rect x="4" y="8" width="38" height="50" fill="none" stroke="#3e8a28" stroke-width="3"/><rect x="14" y="3" width="18" height="9" fill="#3e8a28"/><path d="M10 24l3 3 5-6M10 38l3 3 5-6" stroke="#3e8a28" stroke-width="2.5" fill="none"/><circle cx="40" cy="40" r="13" fill="#fff" stroke="#3e8a28" stroke-width="4"/><path d="M49 50l12 14" stroke="#3e8a28" stroke-width="6"/></svg></div>
    <h3>Document reviews</h3>
    <p>Nam libero tempore, cum soluta nobis<br>est eligendi optio cumque nihi</p>
    <span class="read-more">READ MORE &gt;&gt;</span>
  </div>
  <div class="service" style="left:873px">
    <div class="service-ring"><svg width="64" height="50" viewBox="0 0 64 50"><path d="M6 28l16 16L58 6" stroke="#3e8a28" stroke-width="7" fill="none" stroke-linecap="round" stroke-linejoin="round"/></svg></div>
    <h3>Hands-on-help with tender</h3>
    <p>Nam libero tempore, cum soluta nobis<br>est eligendi optio cumque nihi</p>
    <span class="read-more">READ MORE &gt;&gt;</span>
  </div>
</section>

<section class="blog">
  <h2 class="section-title heading" style="top:1535px">LATEST BLOG</h2>

  <article class="blog-card" style="left:95px">
    <div class="blog-photo"><div class="media" style="background:linear-gradient(135deg,#e9e4dc,#bcc9d8 50%,#f4f4f4)" role="img" aria-label="Colleagues reviewing printed charts at a table"></div>
      <div class="date"><b>01</b><span>NOV</span></div></div>
    <h3>Finibus Bonorum et Malorum</h3>
    <p>Nam libero tempore, cum soluta nobis est eligendi optio cumque nihil impedit quo minus id quod maxim.</p>
    <div class="blog-meta"><span><svg width="11" height="12" viewBox="0 0 11 12"><circle cx="5.5" cy="3" r="3" fill="#3e8a28"/><path d="M0 12a5.5 5 0 0111 0z" fill="#3e8a28"/></svg>Lars Berg</span><span><svg width="15" height="12" viewBox="0 0 15 12"><ellipse cx="7" cy="5" rx="6" ry="4" fill="none" stroke="#3e8a28" stroke-width="1.6"/><path d="M3 8l-2 3 4-2" fill="#3e8a28"/></svg>3 Comments</span></div>
  </article>

  <article class="blog-card" style="left:440px">
    <div class="blog-photo"><div class="media" style="background:linear-gradient(135deg,#d7d7d7,#f2f2f2 45%,#9fb1c6)" role="img" aria-label="Calculator and pen on an insurance form"></div>
      <div class="date"><b>01</b><span>NOV</span></div></div>
    <h3>Finibus Bonorum et Malorum</h3>
    <p>Nam libero tempore, cum soluta nobis est eligendi optio cumque nihil impedit quo minus id quod maxim.</p>
    <div class="blog-meta"><span><svg width="11" height="12" viewBox="0 0 11 12"><circle cx="5.5" cy="3" r="3" fill="#3e8a28"/><path d="M0 12a5.5 5 0 0111 0z" fill="#3e8a28"/></svg>Lars Berg</span><span><svg width="15" height="12" viewBox="0 0 15 12"><ellipse cx="7" cy="5" rx="6" ry="4" fill="none" stroke="#3e8a28" stroke-width="1.6"/><path d="M3 8l-2 3 4-2" fill="#3e8a28"/></svg>3 Comments</span></div>
  </article>

  <article class="blog-card" style="left:783px">
    <div class="blog-photo"><div class="media" style="background:linear-gradient(135deg,#4c5560,#a9b3bc 50%,#3d4248)" role="img" aria-label="Presenter explaining a chart to a team in a meeting room"></div>
      <div class="date"><b>01</b><span>NOV</span></div></div>
    <h3>Finibus Bonorum et Malorum</h3>
    <p>Nam libero tempore, cum soluta nobis est eligendi optio cumque nihil impedit quo minus id quod maxim.</p>
    <div class="blog-meta"><span><svg width="11" height="12" viewBox="0 0 11 12"><circle cx="5.5" cy="3" r="3" fill="#3e8a28"/><path d="M0 12a5.5 5 0 0111 0z" fill="#3e8a28"/></svg>Lars Berg</span><span><svg width="15" height="12" viewBox="0 0 15 12"><ellipse cx="7" cy="5" rx="6" ry="4" fill="none" stroke="#3e8a28" stroke-width="1.6"/><path d="M3 8l-2 3 4-2" fill="#3e8a28"/></svg>3 Comments</span></div>
  </article>
</section>

<section class="testimonials">
  <h2 class="section-title heading">CLIENT TESTIMONIALS</h2>
  <div class="arrow" style="left:28px;top:151px"><svg width="10" height="14"><path d="M8 1L2 7l6 6" stroke="#fff" fill="none" stroke-width="1.5"/></svg></div>
  <div class="arrow" style="left:1134px;top:151px"><svg width="10" height="14"><path d="M2 1l6 6-6 6" stroke="#fff" fill="none" stroke-width="1.5"/></svg></div>

  <div class="quote" style="left:95px">
    <div class="avatar" role="img" aria-label="Portrait of client Maja Holm"></div>
    <div class="quote-body"><p>Nam libero tempore, cum solut nobis est eligendi optio cumque nihil impedi quo minus id quod maxime placeat facere poss imus, omnis voluptas assu.</p><h4>Maja Holm</h4><small>Holm Gård, Ekby Uppland</small></div>
  </div>
  <div class="quote" style="left:440px">
    <div class="avatar" role="img" aria-label="Portrait of client Olof Strand"></div>
    <div class="quote-body"><p>Nam libero tempore, cum solut nobis est eligendi optio cumque nihil impedi quo minus id quod maxime placeat facere poss imus, omnis voluptas assu.</p><h4>Olof Strand</h4><small>aspiring farmer, Norrvik Jämtland</small></div>
  </div>
  <div class="quote" style="left:792px">
    <div class="avatar" role="img" aria-label="Portrait of client Axel Lund"></div>
    <div class="quote-body"><p>Nam libero tempore, cum solut nobis est eligendi optio cumque nihil impedi quo minus id quod maxime placeat facere poss imus, omnis voluptas assu.</p><h4>Axel Lund and Erik Dahl</h4><small>aspiring farmers, Sjöby Halland</small></div>
  </div>
</section>

<footer class="site-footer">
  <div class="abs footer-brand"><span class="brand-dot"></span>Kestrel Analys<br>&amp; Rådgivning</div>

  <div class="abs footer-col" style="left:415px;top:2432px">
    <h4>Information</h4>
    Home<br>About Us<br>Services<br>Industries<br>Resources<br>Blog<br>Contact Us
  </div>

  <div class="abs footer-col" style="left:585px;top:2432px">
    <h4>Newsletter Subscription</h4>
    Register your Email Address to get<br>Information about us
    <div class="email-field">Email Address</div>
    <div class="outline-btn subscribe">SUBSCRIBE</div>
  </div>

  <div class="abs footer-col" style="left:890px;top:2432px">
    <h4>Contact Us</h4>
    <div class="contact-row"><svg width="10" height="14" viewBox="0 0 10 14"><path d="M5 0a5 5 0 00-5 5c0 4 5 9 5 9s5-5 5-9a5 5 0 00-5-5z" fill="#3e8a28"/><circle cx="5" cy="5" r="2" fill="#fff"/></svg><span>27 Lindgatan, Box 412<br>Vretby 114 55</span></div>
    <div class="contact-row"><svg width="12" height="12" viewBox="0 0 24 24"><path fill="#3e8a28" d="M6.6 10.8a15 15 0 006.6 6.6l2.2-2.2c.3-.3.7-.4 1-.2 1.1.4 2.3.6 3.6.6.6 0 1 .4 1 1V20c0 .6-.4 1-1 1A17 17 0 013 4c0-.6.4-1 1-1h3.5c.6 0 1 .4 1 1 0 1.3.2 2.5.6 3.6.1.3 0 .7-.2 1z"/></svg><span>1 555 010 0199</span></div>
    <div class="contact-row"><svg width="13" height="10" viewBox="0 0 13 10"><rect width="13" height="10" fill="#3e8a28"/><path d="M0 0l6.5 5L13 0" stroke="#fff" fill="none"/></svg><span>info@kestrelanalys.se</span></div>
  </div>

  <div class="abs footer-rule"></div>
  <p class="abs copyright">Copyrights © 2017, Kestrel Analys &amp; Rådgivning.  All rights reserved.</p>
  <div class="abs social"><i></i><i></i><i></i><i></i></div>
</footer>

</body>
</html>
```